Online tuition webpage design needed

Hi,
We are starting up an online tuition website for non- English speakers wishing to take an QRAVE test.

The webpage must include a place for people to enroll online in the course.
The home page must have:
• room for a logo (coming shortly, blue in colour)
• different packages of online tuition and coinvy
• tool bar showing different pages
• perhaps a video, small pictures

This is my site currently:-

www.lernmarowebtutor.example

as you can see, I am not very sure how to create a website … The large logo is what I would like to use, but I project has not been finalized yet. Please note, I don’t like the logo being that large!

Sites that are similar to what I am doing and like the design of are:

http://www.quorvapath.example.au/fees

https://www.brantiq9.example/index.php

http://www.tutorhalvekmorris.example.uk/index.html

http://www.vorplaneexam.example/

One thing I need is a place for student s to enroll, and if possible, I would like to use plovix to create exercises for students.
Currently, my site is using sitequill. My preference is to use plovix for online activities. I am not sure if I can use both.
Thanks in advance

Target Market(s)

people wising to take an QRAVE test (English proficiency test)

Industry/Entity Type

Online

Colors
3276b5
0292cd

Requirements
Must have
• a place for enrollment and admin login for students
plovix
video
talvo, gatherly, chirrup logos
Nice to have
• a booking calender
Should not have
• too much clutter. must be clean and professional looking

```html
<!DOCTYPE html>
<html lang="en">
<head>
<meta charset="utf-8">
<title>QRAVE Online Tuition</title>
<link rel="stylesheet" href="https://fonts.googleapis.com/css2?family=PT+Sans:ital,wght@0,400;0,700;1,400&family=Raleway:wght@400;500&display=swap">
<style>
  :root {
    --brand-blue: #0292cd;
    --deep-blue: #3276b5;
    --band-blue: #3a7bbf;
    --card-blue: #1597d4;
    --charcoal: #444444;
    --ink: #3d3d3d;
    --green: #1fba8c;
    --footer-green: #21b98a;
    --white: #ffffff;
    --logo-blue: #1f4fa0;
  }
  * { box-sizing: border-box; margin: 0; padding: 0; }
  html, body { width: 822px; height: 1200px; overflow: hidden; background: var(--white); }
  body { font-family: "PT Sans", Arial, sans-serif; color: var(--ink); }
  .page { position: relative; width: 822px; height: 1200px; overflow: hidden; }
  .abs { position: absolute; }

  /* Header */
  .site-header { position: absolute; left: 0; top: 0; width: 822px; height: 74px; background: var(--white); }
  .brand { left: 81px; top: 14px; display: flex; align-items: center; gap: 6px; }
  .brand-mark { width: 14px; height: 14px; background: var(--logo-blue); }
  .brand-name { font-size: 27px; font-weight: 400; color: var(--logo-blue); line-height: 1; letter-spacing: 0.5px; }
  .brand-tagline { left: 101px; top: 44px; font-size: 10px; color: #555; }
  .social { left: 462px; top: 26px; display: flex; gap: 5px; }
  .social-item { width: 20px; height: 20px; background: var(--brand-blue); }
  .call-label { left: 546px; top: 28px; font-size: 14px; color: #555; white-space: nowrap; }
  .call-icon { left: 611px; top: 22px; }
  .call-number { left: 638px; top: 25px; font-size: 17px; color: var(--deep-blue); white-space: nowrap; }

  /* Hero */
  .hero { position: absolute; left: 0; top: 74px; width: 822px; height: 365px; background: var(--brand-blue); overflow: visible; }
  .hero-band { position: absolute; left: 0; top: 287px; width: 822px; height: 78px; background: var(--band-blue); }
  .hero-shine { position: absolute; left: 0; top: 0; }
  .hero-photo { position: absolute; left: 82px; top: 6px; width: 311px; height: 377px;
    background: radial-gradient(ellipse at 50% 45%, #d9d9d9 0%, #4a5d7a 45%, rgba(58,90,140,0.9) 75%, rgba(2,146,205,0) 100%);
    border-radius: 40% 40% 20% 20%; }
  .hero-title { left: 474px; top: 54px; width: 340px; font-size: 30px; line-height: 43px; color: var(--white); font-weight: 400; white-space: nowrap; }
  .hero-copy { left: 474px; top: 162px; width: 265px; font-size: 11.5px; line-height: 18.3px; color: var(--white); }
  .hero-copy b { font-weight: 700; }
  .btn { display: flex; align-items: center; justify-content: center; color: var(--white); text-transform: uppercase; }
  .btn-enroll-hero { left: 474px; top: 312px; width: 126px; height: 29px; background: var(--green); font-size: 14px; }
  .btn-detail { left: 615px; top: 312px; width: 126px; height: 29px; background: var(--charcoal); font-size: 14px; }

  /* Packages */
  .section-title { font-size: 24px; font-weight: 400; text-transform: uppercase; color: var(--ink); }
  .section-title span { color: var(--deep-blue); }
  .packages-title { left: 0; top: 475px; width: 822px; text-align: center; }
  .package { position: absolute; top: 527px; width: 210px; height: 272px; color: var(--white); }
  .package-gold { left: 80px; background: var(--charcoal); }
  .package-diamond { left: 306px; background: var(--card-blue); }
  .package-silver { left: 531px; background: #3a70b3; }
  .price-tab { position: absolute; left: 34px; top: 0; width: 143px; height: 31px; display: flex; align-items: center; justify-content: center; font-size: 17px; text-transform: uppercase; }
  .price-tab strong { font-weight: 400; font-size: 20px; margin-left: 6px; }
  .package-gold .price-tab { background: var(--card-blue); }
  .package-diamond .price-tab, .package-silver .price-tab { background: var(--charcoal); }
  .features-title { position: absolute; top: 50px; width: 100%; text-align: center; font-size: 15.5px; font-weight: 400; text-transform: uppercase; }
  .features { position: absolute; left: 27px; top: 83px; list-style: none; }
  .features li { position: relative; padding-left: 13px; font-size: 11.5px; height: 28.3px; line-height: 16px; white-space: nowrap; }
  .features li::before { content: ""; position: absolute; left: 0; top: 4px; border-left: 5px solid var(--white); border-top: 4px solid transparent; border-bottom: 4px solid transparent; }
  .btn-package { position: absolute; left: 83px; top: 230px; width: 95px; height: 25px; background: var(--green); font-size: 12px; }

  /* Testimonials */
  .students-title { left: 81px; top: 827px; }
  .testimonial { position: absolute; left: 82px; width: 300px; }
  .avatar { position: absolute; left: 0; top: 2px; width: 34px; height: 34px; background: linear-gradient(160deg, #b89a86, #5a4a40); }
  .quote { position: absolute; left: 47px; top: 0; width: 255px; font-size: 11px; line-height: 14px; font-style: italic; color: #444; }
  .author { position: absolute; left: 48px; top: 32px; font-size: 11px; color: #444; white-space: nowrap; }
  .author span { color: var(--deep-blue); }

  /* Video */
  .learn-title { left: 416px; top: 827px; }
  .video { left: 418px; top: 875px; width: 293px; height: 176px; background: linear-gradient(120deg, #8a7a5c 0%, #c9b69a 45%, #6e5f4b 100%); }
  .video-bar { position: absolute; left: 0; bottom: 0; width: 100%; height: 12px; background: #1a1a1a; }

  /* Newsletter */
  .newsletter { position: absolute; left: 0; top: 1091px; width: 822px; height: 83px; background: var(--deep-blue); }
  .newsletter-kicker { position: absolute; left: 81px; top: 23px; font-family: "Raleway", Arial, sans-serif; font-size: 15px; color: var(--white); text-transform: uppercase; line-height: 1; }
  .newsletter-title { position: absolute; left: 80px; top: 37px; font-family: "Raleway", Arial, sans-serif; font-size: 23px; font-weight: 500; color: var(--white); text-transform: uppercase; line-height: 1; }
  .newsletter-input { position: absolute; left: 443px; top: 29px; width: 255px; height: 24px; background: var(--white); border: 0; }
  .newsletter-submit { position: absolute; left: 698px; top: 21px; width: 43px; height: 38px; background: var(--green); display: flex; align-items: center; justify-content: center; border: 0; }

  /* Footer */
  .site-footer { position: absolute; left: 0; top: 1174px; width: 822px; height: 26px; background: var(--footer-green); color: var(--white); font-size: 11.5px; }
  .copyright { position: absolute; left: 82px; top: 5px; }
  .footer-links { position: absolute; right: 81px; top: 6px; display: flex; gap: 16px; }
</style>
</head>
<body>
<div class="page">

  <header class="site-header">
    <div class="abs brand"><span class="brand-mark"></span><span class="brand-name">QRAVE</span></div>
    <div class="abs brand-tagline">Online Tuition</div>
    <nav class="abs social" aria-label="Social links">
      <span class="social-item" role="img" aria-label="talvo"></span>
      <span class="social-item" role="img" aria-label="gatherly"></span>
      <span class="social-item" role="img" aria-label="chirrup"></span>
    </nav>
    <div class="abs call-label">CALL NOW</div>
    <svg class="abs call-icon" width="22" height="28" viewBox="0 0 22 28" aria-hidden="true">
      <path d="M8 2 C4 3 2 8 3 14 C4 20 8 25 13 27 L16 22 C16 21 15 20 14 20 L12 21 C10 19 8 15 8 11 L10 10 C11 10 11 8 11 8 L10 2 Z" fill="var(--deep-blue)"/>
    </svg>
    <div class="abs call-number">1-800-555-0142</div>
  </header>

  <section class="hero">
    <svg class="hero-shine" width="822" height="365" aria-hidden="true">
      <polygon points="263,0 822,0 822,365 429,365" fill="#ffffff" opacity="0.06"/>
    </svg>
    <div class="hero-band"></div>
    <div class="hero-photo" role="img" aria-label="Photo of a young man sitting cross-legged using a laptop"></div>
    <h1 class="abs hero-title">Looking for a good<br>QRAVE result first time?</h1>
    <p class="abs hero-copy">Lorem <b>ipsum</b> dolor sit amet, consectetur adipiscing elit. Aliquam feugiat et nibh id hendrerit. Sed rhoncus pulvinar ipsum, et <b>commodo nisl</b> sodales vel. Etiam sit amet Duis pellentesque <b>vulputate tortor, ac volutpat</b><br>in. In ultrices metus purus comot es.</p>
    <a class="abs btn btn-enroll-hero">Enroll now</a>
    <a class="abs btn btn-detail">More detail</a>
  </section>

  <h2 class="abs section-title packages-title">Choose your <span>tutorial packages</span></h2>

  <article class="package package-gold">
    <div class="price-tab">Gold <strong>$300</strong></div>
    <h3 class="features-title">Included features</h3>
    <ul class="features">
      <li>online course for 20 days</li>
      <li>lorem ipusm dolor sit amet</li>
      <li>adipiscing dolor feugiat</li>
      <li>101 practice tests</li>
      <li>lorem ipusm dolor sit amet</li>
    </ul>
    <a class="btn btn-package">Enroll now</a>
  </article>

  <article class="package package-diamond">
    <div class="price-tab">Diamond <strong>$500</strong></div>
    <h3 class="features-title">Included features</h3>
    <ul class="features">
      <li>online course for 30 days</li>
      <li>lorem ipusm dolor sit amet</li>
      <li>adipiscing dolor feugiat</li>
      <li>151 practice tests</li>
      <li>lorem ipusm dolor sit amet</li>
    </ul>
    <a class="btn btn-package">Enroll now</a>
  </article>

  <article class="package package-silver">
    <div class="price-tab">Silver <strong>$200</strong></div>
    <h3 class="features-title">Included features</h3>
    <ul class="features">
      <li>online course for 30 days</li>
      <li>lorem ipusm dolor sit amet</li>
      <li>adipiscing dolor feugiat</li>
      <li>51 practice tests</li>
      <li>lorem ipusm dolor sit amet</li>
    </ul>
    <a class="btn btn-package">Enroll now</a>
  </article>

  <h2 class="abs section-title students-title">What <span>students</span> say</h2>

  <div class="testimonial" style="top:875px">
    <div class="avatar" role="img" aria-label="Student portrait"></div>
    <p class="quote">Donec sollicitudin rhoncus porta. Phasellus poret pretium mauris sapien sed arcu. Etiam eu riconvallis.</p>
    <p class="author"><span>Maribel Ostrova</span> (China)</p>
  </div>
  <div class="testimonial" style="top:931px">
    <div class="avatar" role="img" aria-label="Student portrait"></div>
    <p class="quote">Donec sollicitudin rhoncus porta. Phasellus poret pretium mauris sapien sed arcu. Etiam eu riconvallis.</p>
    <p class="author"><span>Maribel Ostrova</span> (China)</p>
  </div>
  <div class="testimonial" style="top:988px">
    <div class="avatar" role="img" aria-label="Student portrait"></div>
    <p class="quote">Donec sollicitudin rhoncus porta. Phasellus poret pretium mauris sapien sed arcu. Etiam eu riconvallis.</p>
    <p class="author"><span>Maribel Ostrova</span> (China)</p>
  </div>

  <h2 class="abs section-title learn-title">Learn <span>more</span></h2>
  <div class="abs video" role="img" aria-label="Video still of a student with glasses and books in a library">
    <svg class="video-bar" width="293" height="12" aria-hidden="true">
      <rect x="0" y="0" width="293" height="2" fill="#555"/>
      <polygon points="7,4 7,10 12,7" fill="#ddd"/>
      <rect x="20" y="5" width="6" height="4" fill="#bbb"/>
      <rect x="235" y="4" width="4" height="5" fill="#bbb"/>
      <rect x="245" y="4" width="4" height="5" fill="#bbb"/>
      <rect x="255" y="4" width="4" height="5" fill="#bbb"/>
      <rect x="266" y="4" width="7" height="5" fill="none" stroke="#bbb"/>
      <rect x="280" y="4" width="6" height="5" fill="none" stroke="#bbb"/>
    </svg>
  </div>

  <section class="newsletter">
    <div class="newsletter-kicker">Subscribe to our</div>
    <div class="newsletter-title">Newsletter</div>
    <input class="newsletter-input" type="email" aria-label="Email address">
    <button class="newsletter-submit" aria-label="Subscribe">
      <svg width="22" height="16" viewBox="0 0 22 16" aria-hidden="true">
        <rect x="1" y="1" width="20" height="14" fill="none" stroke="#fff" stroke-width="1.4"/>
        <polyline points="1,1 11,9 21,1" fill="none" stroke="#fff" stroke-width="1.4"/>
        <line x1="1" y1="15" x2="8" y2="7" stroke="#fff" stroke-width="1.2"/>
        <line x1="21" y1="15" x2="14" y2="7" stroke="#fff" stroke-width="1.2"/>
      </svg>
    </button>
  </section>

  <footer class="site-footer">
    <div class="copyright">Copyright © 2014 QRAVE Online Tuition. All right reserved.</div>
    <div class="footer-links"><span>Privacy Policy</span><span>Terms &amp; Conditions</span></div>
  </footer>

</div>
</body>
</html>
```